Stationery Design Project for Lakemont Kenbu Kai Karate Studio

We Need a Stationery Design for a Karate School Teaching Okinawa Shorin Ryu Karate in Cedarvale, Oregon, U.S.A.

Target Market(s)

Adults Base Western Speaking aged between 25 and 65 yrs, old that handle household budgets

Industry/Entity Type

School

Requirements
Must have
• Name of business: Lakemont Kenbu Kai Karate Studio
Address: Maplecrest Plaza 38214 US Hwy. 61
Cedarvale, Oregon. 33812
Phone # : 555-555-0183
email : Lakemontkenbukaistudio@samplemail.net
Logo - attatched

```html
<!DOCTYPE html>
<html lang="en">
<head>
<meta charset="utf-8">
<title>Lakemont Kenbu Kai Karate Studio – Stationery</title>
<link rel="stylesheet" href="https://fonts.googleapis.com/css2?family=Arimo:ital,wght@0,400;0,700;1,700&family=Questrial&display=swap">
<style>
  :root {
    --ink: #000000;
    --paper: #ffffff;
    --red: #d2232a;
    --card-grey: #6f7072;
    --stripe-grey: #7a7a7a;
    --mark-faint: #e6e6e6;
    --mark-faint-red: #f6dcdc;
    --muted: #c9c9c9;
    --frame: #8a8a8a;
    --body-font: "Arimo", Arial, sans-serif;
    --label-font: "Questrial", "Century Gothic", sans-serif;
  }
  html, body { margin: 0; padding: 0; overflow: hidden; }
  body { background: var(--paper); }
  .canvas {
    position: relative; width: 1200px; height: 1200px; overflow: hidden;
    background: var(--paper); font-family: var(--body-font); color: var(--ink);
  }
  .label {
    position: absolute; font-family: var(--label-font); font-size: 27px; font-weight: 400;
    transform: translateX(-50%); white-space: nowrap; margin: 0; line-height: 1;
  }
  .sheet { position: absolute; background: var(--paper); border: 1px solid var(--frame); box-sizing: border-box; }

  /* Letterhead */
  .letterhead { left: 24px; top: 110px; width: 522px; height: 676px; }
  .letterhead__name { position: absolute; left: 21px; top: 28px; font-size: 16px; }
  .letterhead__rule { position: absolute; left: 20px; top: 46px; width: 478px; height: 3px; background: var(--ink); border-radius: 0 2px 2px 0; }
  .letterhead__contact {
    position: absolute; left: 24px; top: 54px; font-size: 11.5px; white-space: nowrap;
    display: flex; align-items: center; gap: 4px;
  }
  .letterhead__contact b { font-weight: 700; }
  .dot { display: inline-block; width: 10px; height: 10px; border-radius: 50%; background: var(--red); }
  .letterhead__mark { position: absolute; left: 96px; top: 150px; width: 330px; }
  .letterhead__email { position: absolute; left: 0; right: 0; top: 632px; text-align: center; font-size: 12px; font-weight: 700; }

  .faint-mark { text-align: center; }
  .faint-mark__circle { display: block; margin: 0 auto; border-radius: 50%; background: var(--mark-faint-red); }
  .faint-mark__name { display: block; color: var(--mark-faint); font-weight: 700; line-height: 1.05; text-transform: uppercase; }

  /* Envelope front */
  .envelope-front { left: 568px; top: 168px; width: 580px; height: 274px; }
  .envelope-front__band { position: absolute; left: 0; top: 0; right: 0; height: 10px; background: var(--ink); }
  .envelope-front__return { position: absolute; left: 13px; top: 15px; font-size: 9.5px; line-height: 1.1; font-style: normal; }
  .envelope-front__return strong { color: var(--red); }
  .envelope-front__mark { position: absolute; left: 370px; top: 60px; width: 200px; }

  /* Envelope back */
  .envelope-back { position: absolute; left: 568px; top: 511px; }

  /* Business cards */
  .card { position: absolute; top: 925px; width: 304px; height: 174px; box-sizing: border-box; }
  .card--front { left: 253px; background: var(--card-grey); }
  .card--back { left: 620px; border: 1px solid var(--frame); background: var(--paper); }
  .card__holder { position: absolute; left: 14px; top: 14px; color: var(--paper); font-weight: 700; font-size: 13px; }
  .card__role { position: absolute; left: 14px; top: 31px; color: var(--muted); font-weight: 700; font-style: italic; font-size: 11px; }
  .card__address { position: absolute; left: 14px; top: 92px; font-size: 11px; line-height: 1.35; }
  .card__address b { font-weight: 700; }
  .card__phone { color: var(--muted); font-weight: 700; font-size: 12.5px; }
  .card__mark { position: absolute; left: 190px; top: 12px; width: 104px; text-align: center; }
  .card__mark-circle { display: block; width: 38px; height: 38px; margin: 10px auto 8px; border-radius: 50%; background: var(--red); }
  .card__mark-name { display: block; font-weight: 700; font-size: 15px; line-height: 1.05; text-transform: uppercase; color: var(--ink); }
  .card__back-mark { position: absolute; left: 74px; top: 18px; width: 156px; }
</style>
</head>
<body>
<main class="canvas">

  <h2 class="label" style="left:288px; top:50px;">Letterhead</h2>
  <section class="sheet letterhead" aria-label="Letterhead">
    <div class="letterhead__name">Lakemont Kenbu Kai Karate Studio</div>
    <div class="letterhead__rule"></div>
    <div class="letterhead__contact">
      <b>Maplecrest Plaza</b><span class="dot"></span>
      <span>38214 US Hwy. 61</span><span class="dot"></span>
      <span>Cedarvale, Oregon. 33812</span><span class="dot"></span>
      <b>555-555-0183</b>
    </div>
    <div class="letterhead__mark faint-mark" aria-label="Lakemont Kenbu Kai">
      <span class="faint-mark__circle" style="width:120px;height:120px;"></span>
      <span class="faint-mark__name" style="font-size:52px;margin-top:40px;">Lakemont<br>Kenbu Kai</span>
    </div>
    <div class="letterhead__email">Lakemontkenbukaistudio@samplemail.net</div>
  </section>

  <h2 class="label" style="left:862px; top:107px;">Envelope</h2>
  <section class="sheet envelope-front" aria-label="Envelope front">
    <div class="envelope-front__band"></div>
    <address class="envelope-front__return">
      <strong>Lakemont Kenbu Kai Karate Studio</strong><br>
      Maplecrest Plaza<br>
      38214 U.S. Hwy 61<br>
      Cedarvale, Oregon 33812
    </address>
    <div class="envelope-front__mark faint-mark" aria-label="Lakemont Kenbu Kai">
      <span class="faint-mark__circle" style="width:60px;height:60px;"></span>
      <span class="faint-mark__name" style="font-size:26px;margin-top:18px;">Lakemont<br>Kenbu Kai</span>
    </div>
  </section>
  <h2 class="label" style="left:852px; top:450px;">Front</h2>

  <svg class="envelope-back" width="580" height="276" viewBox="0 0 580 276" aria-label="Envelope back">
    <rect x="0.5" y="0.5" width="579" height="275" fill="#fff" stroke="var(--frame)"/>
    <polygon points="0,0 580,0 486,85 80,85" fill="var(--ink)"/>
    <rect x="24" y="20" width="532" height="4" fill="var(--stripe-grey)"/>
    <rect x="52" y="53" width="476" height="4" fill="var(--stripe-grey)"/>
    <line x1="132" y1="85" x2="0" y2="275" stroke="var(--frame)" stroke-width="1"/>
    <line x1="444" y1="85" x2="580" y2="275" stroke="var(--frame)" stroke-width="1"/>
    <circle cx="288" cy="41" r="40" fill="var(--red)"/>
    <text x="288" y="45" text-anchor="middle" font-family="Arimo, Arial, sans-serif" font-weight="700" font-size="10" fill="#fff">LAKEMONT</text>
  </svg>
  <h2 class="label" style="left:866px; top:792px;">Back</h2>

  <h2 class="label" style="left:583px; top:860px;">Business Card</h2>
  <section class="card card--front" aria-label="Business card front">
    <div class="card__holder">Sensei Daniel R. Okafor</div>
    <div class="card__role">Instructor</div>
    <div class="card__address">
      <b>Maplecrest Plaza</b><br>
      38214 U.S. Hwy 61<br>
      Cedarvale, Oregon. 33812<br>
      <span class="card__phone">Phone: 555-555-0183</span><br>
      Email:Lakemontkenbukaistudio@samplemail.net
    </div>
    <div class="card__mark">
      <span class="card__mark-circle"></span>
      <span class="card__mark-name">Lakemont<br>Kenbu Kai</span>
    </div>
  </section>
  <section class="card card--back" aria-label="Business card back">
    <div class="card__back-mark faint-mark" aria-label="Lakemont Kenbu Kai">
      <span class="faint-mark__circle" style="width:50px;height:50px;"></span>
      <span class="faint-mark__name" style="font-size:22px;margin-top:16px;">Lakemont<br>Kenbu Kai</span>
    </div>
  </section>
  <h2 class="label" style="left:400px; top:1112px;">Front</h2>
  <h2 class="label" style="left:768px; top:1108px;">Back</h2>

</main>
</body>
</html>
```